User Interface Designer Needed

I need a few designs for a property law comparison website. We assist the public with finding a solicitor for the purchase or sale of their house and units. We are currently in the process of creating a questionnaire based woo commerce product filter using gravity forms. I'd like to see designs that use the logo colours. Users will be selecting options such as "Buying" or "Selling", they will then be selecting options such as "House" "Unit" or "Land". Details attached. The final design should communicate ease and simplicity. Questions will be answered one at a time, and the next question is dependent on the answer to the question prior

Target Market(s)

First home buyers, people from ages 18-80 make and female looking to get rid of the hassle of ringing around and going from website to website trying to get a quote

Industry/Entity Type

Real Estate

Number of Pages Required

1 page

Colors
33a6d7

Requirements
Must have
• A design for every question
Nice to have
• Simple symbols or simplistic pictures incorporated, even better if you can turn the question into a picture instead of words eg. A picture of a house, a picture of a unit and a picture of land instead of written answers

```html
<!DOCTYPE html>
<html lang="en">
<head>
<meta charset="utf-8">
<title>Nestwise – Quote options</title>
<link href="https://fonts.googleapis.com/css2?family=Roboto:wght@300;400;500;700&display=swap" rel="stylesheet">
<style>
  :root {
    --brand: #33a6d7;
    --ink: #444444;
    --ink-soft: #555555;
    --panel: #f2f2f2;
    --panel-edge: #d9d9d9;
    --card: #ffffff;
    --card-edge: #d4d4d4;
    --rule: #4a4a4a;
    --pick: #3aa935;
    --radio-edge: #c9c9c9;
    --button: #3c4a66;
    --pill-inner: #f4f5f6;
  }
  * { box-sizing: border-box; margin: 0; padding: 0; }
  html, body { width: 933px; height: 1200px; overflow: hidden; background: #ffffff; }
  body { position: relative; font-family: 'Roboto', sans-serif; color: var(--ink); }

  .site-header { position: absolute; left: 0; top: 0; width: 933px; height: 86px; border-bottom: 1.5px solid var(--rule); }
  .brand { position: absolute; left: 40px; top: 22px; display: flex; align-items: center; gap: 8px; color: var(--brand); font-weight: 500; font-size: 30px; letter-spacing: -0.5px; }
  .brand-dot { width: 38px; height: 38px; border-radius: 50%; background: var(--brand); }

  .summary-pill { position: absolute; left: 55px; top: 161px; width: 822px; height: 52px; border: 1.5px solid var(--brand); border-radius: 26px; }
  .summary-inner { position: absolute; left: -1px; top: -1px; width: 440px; height: 51px; border-radius: 26px; background: var(--pill-inner); border: 1px solid #e2e4e6; display: flex; align-items: center; padding-left: 21px; font-size: 16.5px; gap: 7px; }
  .summary-inner .choice { color: var(--brand); }
  .property-icon { width: 44px; height: 44px; border-radius: 50%; background: linear-gradient(#f7d8cf, #cfe9df); border: 2px solid #dcdcdc; }

  .panel { position: absolute; left: 56px; width: 819px; background: var(--panel); border: 1px solid var(--panel-edge); }
  .panel-extension { top: 229px; height: 181px; }
  .panel-contract { top: 429px; height: 96px; }
  .panel-risk { top: 545px; height: 541px; }

  .panel-title { position: absolute; left: 21px; font-size: 16.5px; transform: translateY(-50%); }
  .panel-lead { position: absolute; left: 21px; top: 71px; font-size: 15px; transform: translateY(-50%); }

  .option { position: absolute; display: flex; align-items: center; gap: 12px; font-size: 15px; transform: translateY(-50%); white-space: nowrap; }
  .radio { width: 19px; height: 19px; border-radius: 50%; background: #fff; border: 1px solid var(--radio-edge); display: flex; align-items: center; justify-content: center; }
  .radio.is-selected::after { content: ""; width: 11px; height: 11px; border-radius: 50%; background: var(--pick); }
  .risk-option { font-size: 15.5px; font-weight: 500; color: var(--ink-soft); gap: 13px; }

  .note { position: absolute; background: var(--card); border: 1px solid var(--card-edge); border-radius: 2px; font-size: 12px; font-weight: 300; line-height: 18.7px; color: var(--ink); }
  .note-extension { left: 19px; top: 100px; width: 740px; height: 59px; padding: 9px 20px 0 21px; text-indent: 3px; }
  .note-termination { left: 19px; top: 132px; width: 237px; height: 121px; padding: 19px 20px 0 21px; }
  .note-recession { left: 283px; top: 133px; width: 237px; height: 388px; padding: 26px 14px 0 38px; }
  .note-variation { left: 549px; top: 133px; width: 237px; height: 180px; padding: 18px 14px 0 24px; }
  .note-recession ul { list-style: none; }
  .note-recession li { position: relative; margin-bottom: 18.5px; }
  .note-recession li::before { content: ""; position: absolute; left: -17px; top: 7px; width: 5px; height: 5px; border-radius: 50%; background: #888; }

  .search-button { position: absolute; left: 385px; top: 1121px; width: 163px; height: 40px; background: var(--button); color: #fff; border: none; font-family: 'Roboto', sans-serif; font-weight: 700; font-size: 17px; }
</style>
</head>
<body>
  <header class="site-header">
    <div class="brand"><span class="brand-dot"></span>Nestwise.com.au</div>
  </header>

  <div class="summary-pill">
    <div class="summary-inner">
      <span>I am</span><span class="choice">buying</span>
      <span class="property-icon" role="img" aria-label="House icon"></span>
      <span class="choice">house with Standard searches</span>
    </div>
  </div>

  <section class="panel panel-extension">
    <h2 class="panel-title" style="top:32px;font-weight:400;">Extension</h2>
    <label class="option" style="left:28px;top:69px;"><span class="radio"></span>I want my quote to include unlimited extension</label>
    <label class="option" style="left:443px;top:69px;"><span class="radio is-selected"></span>I only want to pay for extension if I need them</label>
    <p class="note note-extension">Extensions refer to key contract dates that may be extended by either the seller or the buyer. This involves unexpected additional work for the solicitor or conv</p>
  </section>

  <section class="panel panel-contract">
    <h2 class="panel-title" style="top:28px;font-weight:400;">Contract</h2>
    <label class="option" style="left:28px;top:65px;"><span class="radio"></span>I have a signed contract</label>
    <label class="option" style="left:442px;top:64px;"><span class="radio is-selected"></span>I havent signed a&nbsp; contract yet</label>
  </section>

  <section class="panel panel-risk">
    <h2 class="panel-title" style="top:29px;font-weight:400;">Risk</h2>
    <p class="panel-lead">I want my quote to allow for possibility of</p>
    <label class="option risk-option" style="left:28px;top:108px;"><span class="radio"></span>Terminations</label>
    <label class="option risk-option" style="left:291px;top:108px;"><span class="radio is-selected"></span>Deeds of Recessions</label>
    <label class="option risk-option" style="left:558px;top:108px;"><span class="radio"></span>Deed of variations</label>

    <p class="note note-termination">Terminations refer to the fees associated with the contract ending due to the buyer or seller</p>
    <div class="note note-recession">
      <ul>
        <li>A Deed of Recession is a fancy legal word for a document that ‘rescinds’ or ‘takes back’ the agreement in an existing contract so that a new contract can be entered into.</li>
        <li>This normally happens when there are additional people that need to be added or any other changes to important parts of the contract.</li>
        <li>These are not normally expected, and when required can also mean unexpected fees.</li>
      </ul>
    </div>
    <p class="note note-variation">A Deed of variation is a legal document that ‘varies’ the contract. Normally this document is used when the buyer and the seller have agreed to reduce the price being paid for the property.</p>
  </section>

  <button class="search-button" type="button">Search quotes</button>
</body>
</html>
```